Zielgruppe
Vermietung der Ferienwohnung 'Lindenhof' in Waidhofen an der Ybbs.
Zielgruppe:
Einzelpersonen, Paare, Familien, welche die Ferienwohnung mindestens (besser länger als) eine Woche mieten wollen.
Zum Beispiel Begleitpersonen / Angehörige von Patienten des Kurhauses am Mühlbach.
Assistenz-Ärzte, - Lehrer, die für mehrere Wochen/Monate eine Wohnung suchen. Waidhofen hat ein Gymnasium, HTL und HAK.
Aufgabenstellung
DIN lang 2- oder 4-seitig.
Wichtig im Text:
Kein Auto notwendig;
Alle Schulen, das Therapiezentrum und das Stadtzentrum sind zu Fuß in wenigen Minuten zu erreichen, ebenso auch viele Wanderwege und der Sonnentalweg.
Preis (2-6 Nächte) : 1 Person: 60 Euro/Nacht
2 Personen: 75 Euro/Nacht
Preise Langzeitmieten:
1 Woche: 350 Euro
2 Wochen: 500 Euro
ab 1 Monat: 800 Euro/Monat
Endreinigung: 45 Euro
Logo der Lindenhof verwenden.

```html
<!DOCTYPE html>
<html lang="de">
<head>
<meta charset="utf-8">
<title>Ferienwohnung Lindenhof – Flyer DIN lang</title>
<link rel="stylesheet" href="https://fonts.googleapis.com/css2?family=Montserrat:wght@400;500;700&display=swap">
<style>
  :root {
    --green: #67a86a;
    --white: #ffffff;
    --backdrop: #e6e6e6;
    --logo-green: #5a9c5e;
    --logo-blue: #2a4f9c;
  }
  * { margin: 0; padding: 0; box-sizing: border-box; }
  html, body { width: 1200px; height: 2208px; overflow: hidden; }
  body {
    background: var(--backdrop);
    font-family: 'Montserrat', sans-serif;
    color: var(--white);
    position: relative;
  }
  .page {
    position: absolute;
    top: 558px;
    width: 508px;
    height: 990px;
    transform: scale(1.1);
    transform-origin: top left;
    background: var(--white);
    overflow: hidden;
  }
  .page--front { left: 26px; }
  .page--back { left: 606px; }
  .page svg.shapes { position: absolute; inset: 0; }
  .text { position: absolute; }

  .brand { left: 28px; top: 30px; color: var(--logo-blue); }
  .brand__name { font-size: 25px; font-weight: 500; line-height: 1; }
  .brand__url { font-size: 12px; font-weight: 500; color: var(--logo-green); margin-top: 4px; }

  .intro { left: 264px; top: 364px; width: 240px; }
  .intro h1 { font-size: 15px; font-weight: 700; line-height: 1.3; margin-bottom: 3px; }
  .intro p { font-size: 11.5px; line-height: 1.38; margin-bottom: 11px; }
  .intro h2 { font-size: 15.5px; font-weight: 700; margin-top: -1px; }
  .contact-name { font-size: 11.5px; margin-bottom: 8px; }
  .contact-line { display: flex; align-items: center; gap: 7px; font-size: 11.5px; margin-bottom: 8px; white-space: nowrap; }
  .contact-line svg { flex: none; }
  .contact-line--indent { padding-left: 62px; }

  .prices { left: 27px; top: 354px; width: 220px; }
  .prices h2 { font-size: 15px; font-weight: 700; margin-bottom: 2px; }
  .prices p { font-size: 11.5px; line-height: 1.38; }
  .prices .gap { margin-top: 13px; }
  .contact { left: 255px; top: 392px; width: 250px; }
  .contact h2 { font-size: 21px; font-weight: 700; margin-bottom: 4px; }
  .contact .contact-name { font-size: 14.5px; margin-bottom: 10px; }
</style>
</head>
<body>

<section class="page page--front">
  <svg class="shapes" width="508" height="990" viewBox="0 0 508 990">
    <defs>
      <linearGradient id="room-dining" x1="0" y1="0" x2="0.3" y2="1">
        <stop offset="0" stop-color="#f4efe4"/>
        <stop offset="0.3" stop-color="#e9dcc4"/>
        <stop offset="0.55" stop-color="#d9b36c"/>
        <stop offset="0.75" stop-color="#c88a3e"/>
        <stop offset="1" stop-color="#9c5a24"/>
      </linearGradient>
      <linearGradient id="plan" x1="0" y1="0" x2="1" y2="1">
        <stop offset="0" stop-color="#f1ece4"/>
        <stop offset="0.35" stop-color="#d18a4f"/>
        <stop offset="0.7" stop-color="#c4773f"/>
        <stop offset="1" stop-color="#ece6dc"/>
      </linearGradient>
      <linearGradient id="room-living" x1="0" y1="0" x2="0.2" y2="1">
        <stop offset="0" stop-color="#f3ede2"/>
        <stop offset="0.35" stop-color="#ead8bd"/>
        <stop offset="0.6" stop-color="#d89c5a"/>
        <stop offset="0.8" stop-color="#c56f3a"/>
        <stop offset="1" stop-color="#a2542a"/>
      </linearGradient>
    </defs>
    <polygon points="0,170 508,0 508,262 0,432" fill="url(#room-dining)" role="img" aria-label="Foto: Wohn- und Essbereich mit Esstisch und rotem Sofa"/>
    <rect x="22" y="440" width="218" height="196" fill="url(#plan)" role="img" aria-label="Grundriss der Wohnung mit Küche, Wohnen/Essen, Schlafen, Bad und WC"/>
    <polygon points="254,352 508,268 508,806 254,740" fill="var(--green)"/>
    <polygon points="0,650 508,812 508,990 0,990" fill="url(#room-living)" role="img" aria-label="Foto: Wohnzimmer unter der Dachschräge mit rotem Sofa und Sesseln"/>
  </svg>

  <div class="text brand">
    <div class="brand__name">Lindenhof</div>
    <div class="brand__url">ferienwohnung-lindenhof.at</div>
  </div>

  <div class="text intro">
    <h1>Vermietung der Ferienwohnung 'Lindenhof' in Waidhofen an der Ybbs.</h1>
    <p>Unsere Ferienwohnung 'Lindenhof' bietet ihnen auf 80 m² alles, was Sie für einen erholsamen Aufenthalt mit bis zu 4 Erwachsenen benötigen.</p>
    <p>Die Ferienwohnung ist auch oder gerade für Gäste ohne Auto sehr gut geeignet.</p>
    <p>Unser Domizil ist der ideale Ausgangspunkt für vielfältige Unternehmungen zu jeder Jahreszeit für Alt und Jung, Familien mit Kindern oder auch Gästen mit Hund.</p>
    <h2>Kontakt</h2>
    <div class="contact-name">Stefan Kogler</div>
    <div class="contact-line">
      <svg width="20" height="20" viewBox="0 0 20 20"><circle cx="10" cy="10" r="10" fill="#fff"/><path d="M6.5 5.5l2 2-1 1.5c.8 1.6 1.9 2.7 3.5 3.5l1.5-1 2 2-1.2 1.5c-3.6-.4-6.9-3.7-7.3-7.3z" fill="var(--green)"/></svg>
      info@ferienwohnung-lindenhof.at
    </div>
    <div class="contact-line contact-line--indent">
      <svg width="20" height="20" viewBox="0 0 20 20"><circle cx="10" cy="10" r="10" fill="#fff"/><rect x="5" y="6.5" width="10" height="7" fill="none" stroke="var(--green)" stroke-width="1.3"/><path d="M5 6.5l5 4 5-4" fill="none" stroke="var(--green)" stroke-width="1.3"/></svg>
      +43 664 5120478
    </div>
  </div>
</section>

<section class="page page--back">
  <svg class="shapes" width="508" height="990" viewBox="0 0 508 990">
    <defs>
      <linearGradient id="town" x1="0" y1="0" x2="0.15" y2="1">
        <stop offset="0" stop-color="#4a78c0"/>
        <stop offset="0.22" stop-color="#86aad6"/>
        <stop offset="0.36" stop-color="#9a8f7c"/>
        <stop offset="0.5" stop-color="#d6d2c8"/>
        <stop offset="0.68" stop-color="#b89a84"/>
        <stop offset="0.82" stop-color="#5e7f45"/>
        <stop offset="1" stop-color="#1f3350"/>
      </linearGradient>
      <linearGradient id="kitchen" x1="0" y1="0" x2="0" y2="1">
        <stop offset="0" stop-color="#e7d7a8"/>
        <stop offset="0.45" stop-color="#eef0ee"/>
        <stop offset="0.8" stop-color="#d8dadb"/>
        <stop offset="1" stop-color="#b58b58"/>
      </linearGradient>
      <linearGradient id="bedroom" x1="0" y1="0" x2="0" y2="1">
        <stop offset="0" stop-color="#ece6dc"/>
        <stop offset="0.45" stop-color="#f1e3c8"/>
        <stop offset="0.7" stop-color="#f7f5f2"/>
        <stop offset="1" stop-color="#dcdde2"/>
      </linearGradient>
      <linearGradient id="house" x1="0" y1="0" x2="0" y2="1">
        <stop offset="0" stop-color="#6f9bd2"/>
        <stop offset="0.2" stop-color="#6a5848"/>
        <stop offset="0.35" stop-color="#b89d78"/>
        <stop offset="0.85" stop-color="#a98f6c"/>
        <stop offset="1" stop-color="#8c8a86"/>
      </linearGradient>
    </defs>
    <rect width="508" height="990" fill="var(--green)"/>
    <polygon points="0,0 508,0 508,436 0,270" fill="#fff"/>
    <polygon points="0,0 508,0 508,420 0,256" fill="url(#town)" role="img" aria-label="Foto: Altstadt von Waidhofen an der Ybbs mit Kirchturm am Fluss"/>
    <rect x="24" y="542" width="222" height="200" fill="#fff"/>
    <rect x="28" y="546" width="214" height="192" fill="url(#kitchen)" role="img" aria-label="Foto: Küche mit Fenster und Herd"/>
    <rect x="262" y="542" width="223" height="200" fill="#fff"/>
    <rect x="266" y="546" width="215" height="192" fill="url(#bedroom)" role="img" aria-label="Foto: Schlafzimmer mit Doppelbett"/>
    <rect x="92" y="762" width="323" height="201" fill="#fff"/>
    <rect x="96" y="766" width="315" height="193" fill="url(#house)" role="img" aria-label="Foto: Außenansicht des Hauses"/>
  </svg>

  <div class="text prices">
    <h2>Preis (2-6 Nächte):</h2>
    <p>1 Person: 60 Euro/Nacht<br>2 Personen: 75 Euro/Nacht</p>
    <h2 class="gap">Preise Langzeitmieten:</h2>
    <p>1 Woche: 350 Euro<br>2 Wochen: 500 Euro<br>ab 1 Monat: 800 Euro/Monat</p>
    <p class="gap">Endreinigung: 45 Euro</p>
  </div>

  <div class="text contact">
    <h2>Kontakt</h2>
    <div class="contact-name">Stefan Kogler</div>
    <div class="contact-line">
      <svg width="20" height="20" viewBox="0 0 20 20"><circle cx="10" cy="10" r="10" fill="#fff"/><rect x="5" y="6.5" width="10" height="7" fill="none" stroke="var(--green)" stroke-width="1.3"/><path d="M5 6.5l5 4 5-4" fill="none" stroke="var(--green)" stroke-width="1.3"/></svg>
      +43 664 5120478
    </div>
    <div class="contact-line">
      <svg width="20" height="20" viewBox="0 0 20 20"><circle cx="10" cy="10" r="10" fill="#fff"/><path d="M6.5 5.5l2 2-1 1.5c.8 1.6 1.9 2.7 3.5 3.5l1.5-1 2 2-1.2 1.5c-3.6-.4-6.9-3.7-7.3-7.3z" fill="var(--green)"/></svg>
      info@ferienwohnung-lindenhof.at
    </div>
  </div>
</section>

</body>
</html>
```